Website for Dental Office - The Bright Harbor Clinic

The bright harbor clinic is a dental office offering cosmetic dentistry, general dentistry, and multi-specialty dental care all under one roof in our state-of-the-art cosmetic dental center. We are particularly striving to provide services that fit the need of the young generation. Thus, we hope to have a modern, professional concise website that represents our spirit.

*Should be able to switch from English to Chinese

6 sections besides homepage:
Home, Meet us, Services,
Patient Info, Cases&Reviews, Blog, Contact

The Services sections should contain multiple subsections such as cleaning and prevention, cosmetic dentistry, implant dentistry, removable dentures, etc...
The Patient Info section is also intended to contain several subsections such as
New Patient offer, accepted Insurance, patient portal, helpful tips, etc...

Target Market(s)

young generation

Coding

Coded - Design and coding required

Number of Pages Required

5+ page

Font styles to use
Sans Serif

Colors
0592cd
33a6d7
85cae6
00a990
33b8a4
86cfc6
cee9f5
cfeae6
3277b5

Requirements
Must have
• *Should be able to switch from English to Chinese
Nice to have
• http://www.thebrightharborclinic.example/
• As a reference, the above link is the current website, but we would like to change the appearance and the content (our new logo's picture is attached)

```html
<!DOCTYPE html>
<html lang="en">
<head>
<meta charset="utf-8">
<title>The Bright Harbor Clinic</title>
<link href="https://fonts.googleapis.com/css2?family=Nunito:wght@700;800;900&family=Nunito+Sans:wght@400;600;700;800&family=Libre+Baskerville:ital,wght@1,400;1,700&display=swap" rel="stylesheet">
<style>
:root{
  --blue:#33a6d7;
  --blue-deep:#0592cd;
  --blue-light:#85cae6;
  --blue-pale:#cee9f5;
  --navy:#1d5f7f;
  --green:#00a990;
  --green-soft:#33b8a4;
  --text:#3a3a3a;
  --muted:#6b6b6b;
  --footer:#2b2b2b;
  --white:#ffffff;
}
*{box-sizing:border-box;margin:0;padding:0}
html,body{width:1200px;height:3125px;overflow:hidden}
body{position:relative;font-family:"Nunito Sans",sans-serif;color:var(--text);background:var(--white)}
a{color:inherit;text-decoration:none}

/* top bar */
.topbar{position:absolute;left:0;top:0;width:1200px;height:31px;background:var(--green);color:var(--white);font-size:10px;font-weight:600}
.topbar .item{position:absolute;top:9px;display:flex;align-items:center;gap:5px;white-space:nowrap}
.lang{position:absolute;left:910px;top:6px;width:55px;height:19px;border:1px solid rgba(255,255,255,.8);border-radius:10px;display:flex;align-items:center;justify-content:center;gap:4px;font-size:9px}

/* header */
.header{position:absolute;left:0;top:31px;width:1200px;height:88px;background:var(--white)}
.brand{position:absolute;left:233px;top:22px;display:flex;align-items:center;gap:12px}
.brand-mark{width:46px;height:46px;background:var(--blue-light);border-radius:4px}
.brand-name{font-family:"Nunito",sans-serif;font-weight:800;font-size:19px;line-height:22px;color:var(--blue);text-transform:uppercase;white-space:nowrap}
.nav{position:absolute;left:523px;top:0;height:88px;display:flex;gap:18px;align-items:center;font-size:10px;font-weight:800;letter-spacing:.3px;color:#222;white-space:nowrap}
.nav a{position:relative;height:88px;line-height:96px}
.nav a.active{color:var(--blue)}
.nav a.active::after{content:"";position:absolute;left:0;right:0;bottom:0;height:2px;background:var(--blue)}

/* hero */
.hero{position:absolute;left:0;top:119px;width:1200px;height:438px;background:linear-gradient(100deg,#cfd3d6 0%,#e9e6e3 35%,#f1e3d8 55%,#d9e6ef 80%,#5aa7dd 100%)}
.hero-panel{position:absolute;left:212px;top:130px;width:340px;height:182px;background:rgba(255,255,255,.35);border-radius:12px}
.hero-title{position:absolute;left:233px;top:133px;font-family:"Nunito",sans-serif;font-weight:900;font-size:41px;line-height:45px;color:var(--navy);letter-spacing:.5px}
.hero-sub{position:absolute;left:233px;top:224px;font-size:19px;color:#222}
.btn{position:absolute;display:flex;align-items:center;background:var(--blue);color:var(--white);font-weight:800;font-size:12px;text-transform:uppercase;border-radius:2px;white-space:nowrap}
.btn .tab{width:38px;height:100%;background:var(--blue-light);margin-right:12px}
.slide-arrow{position:absolute;top:207px;width:44px;height:49px;background:var(--blue);display:flex;align-items:center;justify-content:center}
.dots{position:absolute;display:flex;gap:6px;align-items:center}
.dots span{width:7px;height:7px;border-radius:50%;background:var(--blue-light)}
.dots span.on{width:11px;height:11px;background:var(--blue);box-shadow:0 0 0 2px #fff inset}

/* section heading */
.eyebrow{position:absolute;left:0;width:1200px;text-align:center;font-family:"Nunito",sans-serif;font-weight:800;font-size:15px;color:var(--green);text-transform:uppercase}
.sec-title{position:absolute;left:0;width:1200px;text-align:center;font-family:"Nunito",sans-serif;font-weight:900;font-size:26px;color:var(--blue);text-transform:uppercase;letter-spacing:.3px}

/* welcome */
.welcome-text{position:absolute;left:340px;top:710px;width:520px;text-align:center;font-size:11.2px;line-height:18.7px;color:#333}
.welcome-text p+p{margin-top:18.7px}

/* services */
.services{position:absolute;left:0;top:997px;width:1200px;height:520px;background:linear-gradient(90deg,#eaebec 0%,#f3f3f3 40%,#ececec 70%,#e2e4e6 100%)}
.svc-card{position:absolute;width:169px;background:var(--white);text-align:center;box-shadow:0 2px 8px rgba(0,0,0,.05)}
.svc-icon{margin:0 auto;border-radius:50%;background:var(--blue-pale)}
.svc-card h3{font-size:10.5px;font-weight:800;color:#222;margin-top:20px;letter-spacing:.2px}
.svc-card p{font-size:8.8px;line-height:13.8px;color:#555;margin:10px 14px 0}
.svc-more{display:inline-block;font-size:8.5px;font-weight:800;color:var(--blue);margin-top:18px}
.svc-card.featured .svc-more{border:1px solid var(--blue);padding:5px 8px}
.svc-arrow{position:absolute;top:1302px;width:22px;height:22px;background:#c9ccd0;display:flex;align-items:center;justify-content:center}

/* dentists */
.dentist{position:absolute;width:260px;text-align:center}
.dentist .photo{width:119px;height:119px;margin:0 auto;border-radius:50%;border:3px solid var(--blue);padding:4px}
.dentist .photo div{width:100%;height:100%;border-radius:50%;background:linear-gradient(160deg,#c9b3a4,#6b5447)}
.dentist h3{font-size:15.5px;font-weight:800;color:#222;margin-top:20px;white-space:nowrap}
.dentist p{font-size:10px;line-height:13px;color:#666;margin-top:8px}

/* reviews */
.reviews{position:absolute;left:0;top:1906px;width:1200px;height:435px;background:linear-gradient(90deg,#2aa0d6 0%,#38a7d9 45%,#4fb2dd 100%)}
.reviews .eyebrow,.reviews .sec-title{color:var(--white)}
.reviewer{position:absolute;left:0;top:197px;width:1200px;text-align:center;font-family:"Nunito",sans-serif;font-weight:800;font-size:15px;color:var(--white)}
.stars{position:absolute;left:0;top:216px;width:1200px;text-align:center;color:#f7c600;font-size:14px;letter-spacing:2px}
.quote-mark{position:absolute;top:228px;font-family:"Libre Baskerville",serif;font-size:64px;color:var(--white);line-height:1}
.review-text{position:absolute;left:336px;top:246px;width:528px;text-align:center;font-family:"Libre Baskerville",serif;font-style:italic;font-size:10.6px;line-height:20px;color:var(--white)}
.reviews .dots span{width:5px;height:5px;background:rgba(255,255,255,.6)}
.reviews .dots span.on{background:var(--white);box-shadow:none}

/* blog */
.post{position:absolute;top:2499px;width:231px}
.post .thumb{position:relative;height:139px}
.post .tag{position:absolute;left:8px;bottom:10px;height:20px;background:var(--green);color:var(--white);font-size:8.5px;font-weight:800;display:flex;align-items:center;gap:12px;padding:0 8px}
.post h3{font-size:11px;font-weight:800;color:#222;margin-top:21px}
.post p{font-size:10px;line-height:14.5px;color:#333;margin-top:6px}
.post .more{display:block;font-size:8.5px;font-weight:800;color:var(--blue);margin-top:22px}

/* footer */
.footer{position:absolute;left:0;top:2790px;width:1200px;height:335px;background:var(--footer);color:#ddd}
.f-col{position:absolute;top:56px}
.f-col h4{font-size:11px;font-weight:800;color:var(--white);letter-spacing:.3px}
.f-col ul{list-style:none;margin-top:15px;font-size:9.5px;line-height:21.2px}
.f-col li .dash{display:inline-block;width:17px;color:#aaa}
.f-contact{font-size:9.5px;line-height:15px;margin-top:17px}
.hours td{font-size:9.3px;height:21.2px;padding:0}
.hours td.day{width:58px;padding-left:2px}
.hours td.sep{width:16px;color:#aaa}
.social{display:flex;gap:5px;margin-top:15px}
.social span{width:18px;height:18px;border-radius:50%;background:var(--blue)}
.f-rule{position:absolute;left:234px;top:263px;width:732px;height:1px;background:#3d3d3d}
.copyright{position:absolute;left:0;top:287px;width:1200px;text-align:center;font-size:8.5px;color:#ccc}
</style>
</head>
<body>

<!-- Top bar -->
<div class="topbar">
  <div class="item" style="left:233px">
    <svg width="10" height="10" viewBox="0 0 24 24"><path d="M6.6 10.8a15 15 0 0 0 6.6 6.6l2.2-2.2c.3-.3.7-.4 1-.2 1.1.4 2.3.6 3.6.6.6 0 1 .4 1 1V20c0 .6-.4 1-1 1A17 17 0 0 1 3 4c0-.6.4-1 1-1h3.5c.6 0 1 .4 1 1 0 1.3.2 2.5.6 3.6.1.3 0 .7-.2 1z" fill="#fff"/></svg>
    1-555-010-0133
  </div>
  <div class="item" style="left:338px">
    <svg width="12" height="9" viewBox="0 0 12 9"><rect x=".5" y=".5" width="11" height="8" fill="none" stroke="#fff"/><path d="M.5 .5 6 5l5.5-4.5" fill="none" stroke="#fff"/></svg>
    info@brightharborclinic.example
  </div>
  <div class="item" style="left:736px">
    <svg width="10" height="10" viewBox="0 0 10 10"><circle cx="5" cy="5" r="4.3" fill="none" stroke="#fff"/><path d="M5 2.5V5h2" fill="none" stroke="#fff"/></svg>
    Tue-Thu-Fri-Sat: 9:00AM-5:00PM
  </div>
  <div class="lang">
    <svg width="9" height="9" viewBox="0 0 10 10"><circle cx="5" cy="5" r="4.5" fill="#fff"/></svg>
    EN
    <svg width="6" height="4" viewBox="0 0 6 4"><path d="M.5.5 3 3 5.5.5" fill="none" stroke="#fff"/></svg>
  </div>
</div>

<!-- Header -->
<header class="header">
  <div class="brand">
    <div class="brand-mark"></div>
    <div class="brand-name">The Bright Harbor<br>Clinic</div>
  </div>
  <nav class="nav">
    <a class="active">HOME</a>
    <a>MEET US</a>
    <a>SERVICES</a>
    <a>PATIENT INFO</a>
    <a>CASES&amp;REVIEWS</a>
    <a>BLOG</a>
    <a>CONTACT</a>
  </nav>
</header>

<!-- Hero -->
<section class="hero" role="img" aria-label="Photo of a smiling patient in a dental chair with a dentist beside her">
  <div class="hero-panel"></div>
  <h1 class="hero-title">HEALTHY SMILES<br>EVERYDAY</h1>
  <div class="hero-sub">Because your smile is our pasion</div>
  <a class="btn" style="left:233px;top:275px;width:221px;height:37px"><span class="tab"></span>Book my appointment</a>
  <div class="slide-arrow" style="left:82px">
    <svg width="12" height="18" viewBox="0 0 12 18"><path d="M10 2 3 9l7 7" fill="none" stroke="#fff" stroke-width="2.2"/></svg>
  </div>
  <div class="slide-arrow" style="left:1058px">
    <svg width="12" height="18" viewBox="0 0 12 18"><path d="M2 2l7 7-7 7" fill="none" stroke="#fff" stroke-width="2.2"/></svg>
  </div>
  <div class="dots" style="left:571px;top:387px"><span class="on"></span><span></span><span></span><span></span></div>
</section>

<!-- Welcome -->
<section>
  <div class="eyebrow" style="top:606px">Welcome to</div>
  <h2 class="sec-title" style="top:626px">The Bright Harbor Clinic</h2>
  <div class="welcome-text">
    <p>Welcome to The Bright Harbor Clinic where we specialize in General and Cosmetic Dentistry, Dental Implants, Periodontics (Gum Surgery), Endodontics (Root Canal Treatment) and Reconstructive Dentistry for patients in Boston, Brookline, Cambridge, Brighton, Allston, Newton, Watertown, Wellesley and all other surrounding neighborhoods of Boston, Massachusetts.</p>
    <p>With Northfield and Westbrook credentials that inspire confidence, we offer cosmetic dentistry, general dentistry and multi-specialty dental care all under one roof in our state-of-the-art cosmetic dental center conveniently located near Harbor Square on Harbor Lane steps from the city metro. Our specialist are also trained in providing wrinkle relaxers and Dermal Fillers and we would be honored to have you a part of our growing family.</p>
  </div>
  <a class="btn" style="left:489px;top:913px;width:219px;height:36px"><span class="tab"></span>Book my appointment</a>
</section>

<!-- Services -->
<section class="services" role="img" aria-label="Faded photo of a dentist treating a patient"></section>
<div class="eyebrow" style="top:1047px">What we do</div>
<h2 class="sec-title" style="top:1067px">Our Services</h2>

<div class="svc-arrow" style="left:177px"><svg width="6" height="9" viewBox="0 0 6 9"><path d="M5 1 1.5 4.5 5 8" fill="none" stroke="#fff" stroke-width="1.4"/></svg></div>
<div class="svc-arrow" style="left:1001px"><svg width="6" height="9" viewBox="0 0 6 9"><path d="M1 1l3.5 3.5L1 8" fill="none" stroke="#fff" stroke-width="1.4"/></svg></div>

<div class="svc-card" style="left:234px;top:1185px;height:256px;padding-top:28px">
  <div class="svc-icon" style="width:52px;height:52px" role="img" aria-label="Clean tooth icon"></div>
  <h3>CLEANING AND PREVENTION</h3>
  <p>A beautiful, healthy smile that lasts a lifetime is our ultimate goal when treating patients. Your personal home care plays an important role in achieving that goal.</p>
  <a class="svc-more">READ MORE &nbsp;»</a>
</div>
<div class="svc-card" style="left:421px;top:1185px;height:256px;padding-top:28px">
  <div class="svc-icon" style="width:52px;height:52px" role="img" aria-label="Tooth with veneer icon"></div>
  <h3>COSMETIC DENTISTRY</h3>
  <p>Veneers are very thin pieces of durable, tooth shaped porcelain that are custom made and bonded onto the front of teeth to create a beautiful and attractive smile.</p>
  <a class="svc-more">READ MORE &nbsp;»</a>
</div>
<div class="svc-card featured" style="left:609px;top:1167px;height:291px;padding-top:34px;box-shadow:0 6px 18px rgba(0,0,0,.08)">
  <div class="svc-icon" style="width:67px;height:67px;background:var(--blue)" role="img" aria-label="Dental implant icon"></div>
  <h3>IMPLANT DENTISTRY</h3>
  <p>Dental implants are a great way to replace missing teeth and also provide a fixed solution to having removable partial or complete dentures. Implants provide excellent</p>
  <a class="svc-more">READ MORE &nbsp;»</a>
</div>
<div class="svc-card" style="left:795px;top:1185px;height:256px;padding-top:28px">
  <div class="svc-icon" style="width:52px;height:52px" role="img" aria-label="Denture icon"></div>
  <h3>REMOVABLE DENTURES</h3>
  <p>Removable partial dentures are used when only a few teeth are missing and there are still natural teeth present in the mouth. The missing teeth are replaced</p>
  <a class="svc-more">READ MORE &nbsp;»</a>
</div>

<!-- Dentists -->
<div class="eyebrow" style="top:1562px">Meet us</div>
<h2 class="sec-title" style="top:1582px">Meet Our Dentists</h2>

<div class="dentist" style="left:216px;top:1677px">
  <div class="photo"><div role="img" aria-label="Portrait photo of the orthodontist"></div></div>
  <h3>LENA MORADI, DMD, MS</h3>
  <p>Board Certified Orthodontist</p>
</div>
<div class="dentist" style="left:469px;top:1677px">
  <div class="photo"><div role="img" aria-label="Portrait photo of the pediatric dentist"></div></div>
  <h3>VICTOR A. HALE, DMD</h3>
  <p>Board Certified Pediatric Dentist<br>Board Certified Orthodontist</p>
</div>
<div class="dentist" style="left:722px;top:1677px">
  <div class="photo"><div role="img" aria-label="Portrait photo of the general dentist"></div></div>
  <h3>DR. NOOR SALEM, DMD</h3>
  <p>General Dentist</p>
</div>

<!-- Reviews -->
<section class="reviews" role="img" aria-label="Blue-tinted photo of a patient smiling at the dentist">
  <div class="eyebrow" style="top:71px">Reviews</div>
  <h2 class="sec-title" style="top:91px">What Our Patients Say</h2>
  <div class="reviewer">GRANT ELLERY</div>
  <div class="stars">★★★★★</div>
  <div class="quote-mark" style="left:263px">“</div>
  <div class="quote-mark" style="left:902px">”</div>
  <p class="review-text">This place is the best dentist ever. I've had a lot of other dentist but none quite like this place! Shes so funny and she shakes it all the time (Like an instant camera). We are always having a good time, laughing, joking, and just all around havin fun in this office! not to mention its so clean and state of the art. The dentists there were always helping and explaining the process and made me very comfortable.</p>
  <div class="dots" style="left:576px;top:356px"><span class="on"></span><span></span><span></span><span></span></div>
</section>

<!-- Blog -->
<div class="eyebrow" style="top:2387px">Blog</div>
<h2 class="sec-title" style="top:2407px">Latest Blog Posts</h2>

<article class="post" style="left:234px">
  <div class="thumb" role="img" aria-label="Photo of a smiling patient during a dental check-up" style="background:linear-gradient(120deg,#4c93c8,#e6d3c6 55%,#7fb8de)">
    <span class="tag"><span>13 AUG, 2019</span><span>● 10</span></span>
  </div>
  <h3>LOREM IPSUM DOLOR</h3>
  <p>Lorem ipsum dolor sit amet, consectetur adipiscing elit. Quisque iaculis elementum eleifend. Cras malesuada vitae enim id imperdiet.</p>
  <a class="more">READ MORE</a>
</article>
<article class="post" style="left:483px">
  <div class="thumb" role="img" aria-label="Photo of a dentist examining a young girl" style="background:linear-gradient(120deg,#b9c3cc,#e7e2de 50%,#6fa7d6)">
    <span class="tag"><span>13 AUG, 2019</span><span>● 10</span></span>
  </div>
  <h3>LOREM IPSUM DOLOR</h3>
  <p>Lorem ipsum dolor sit amet, consectetur adipiscing elit. Quisque iaculis elementum eleifend. Cras malesuada vitae enim id imperdiet.</p>
  <a class="more">READ MORE</a>
</article>
<article class="post" style="left:733px">
  <div class="thumb" role="img" aria-label="Photo of a smiling woman seated in a dental chair" style="background:linear-gradient(120deg,#e5e7e9,#f1ebe4 50%,#bfc6cc)">
    <span class="tag"><span>13 AUG, 2019</span><span>● 10</span></span>
  </div>
  <h3>LOREM IPSUM DOLOR</h3>
  <p>Lorem ipsum dolor sit amet, consectetur adipiscing elit. Quisque iaculis elementum eleifend. Cras malesuada vitae enim id imperdiet.</p>
  <a class="more">READ MORE</a>
</article>

<!-- Footer -->
<footer class="footer">
  <div class="f-col" style="left:233px">
    <h4>CONTACT</h4>
    <div class="f-contact">
      48 Harbor Lane<br>Suite 210<br>Eastport, MA 02000<br><br>
      <b>Tel:</b> <u>1-555-010-0133</u><br>
      Fax: 1-555-010-0187<br>
      Email: info@brightharborclinic.example
    </div>
  </div>
  <div class="f-col" style="left:422px">
    <h4>OFFICE HOURS</h4>
    <table class="hours" style="margin-top:13px;border-collapse:collapse">
      <tr><td class="day">Monday</td><td class="sep">-</td><td>CLOSED</td></tr>
      <tr><td class="day">Tuesday</td><td class="sep">-</td><td>9:30 am - 5:00 pm</td></tr>
      <tr><td class="day">Wednesday</td><td class="sep">-</td><td>CLOSED</td></tr>
      <tr><td class="day">Thursday</td><td class="sep">-</td><td>9:30 am - 5:00 pm</td></tr>
      <tr><td class="day">Friday</td><td class="sep">-</td><td>9:30 am - 5:00 pm</td></tr>
      <tr><td class="day">Saturday</td><td class="sep">-</td><td>9:30 am - 5:00 pm</td></tr>
      <tr><td class="day">Sunday</td><td class="sep">-</td><td>CLOSED</td></tr>
    </table>
  </div>
  <div class="f-col" style="left:632px">
    <h4>QUICK LINKS</h4>
    <ul>
      <li><span class="dash">-</span>Home</li>
      <li><span class="dash">-</span>Meet us</li>
      <li><span class="dash">-</span>Services</li>
      <li><span class="dash">-</span>Patient Info</li>
      <li><span class="dash">-</span>Cases &amp; Reviews</li>
      <li><span class="dash">-</span>Blog</li>
      <li><span class="dash">-</span>Contact</li>
    </ul>
  </div>
  <div class="f-col" style="left:762px">
    <h4>SUPPORT</h4>
    <ul>
      <li><span class="dash">-</span>Privacy Policy</li>
      <li><span class="dash">-</span>Disclaimer</li>
      <li><span class="dash">-</span>FAQ</li>
    </ul>
  </div>
  <div class="f-col" style="left:877px">
    <h4>FOLLOW US</h4>
    <div class="social"><span></span><span></span><span></span><span></span></div>
  </div>
  <div class="f-rule"></div>
  <div class="copyright">Copyright © 2019 &nbsp;The Bright Harbor Clinic &nbsp;| &nbsp;All rights reserved.</div>
</footer>

</body>
</html>
```